Buch-/E-Book-Cover für Finanzratgeber
Zielgruppe
Wir helfen Menschen dabei, ihr Geld vor der Inflation und den nahenden Enteignung zu schützen.
Aufgabenstellung
Orientierung an den Bestsellern von Finanzprodukten. Komplementärfarben, soll Neugierig machen.

```html
<!DOCTYPE html>
<html lang="de">
<head>
<meta charset="utf-8">
<title>Werden sie uns alles wegnehmen? – Buchumschlag</title>
<link rel="stylesheet" href="https://fonts.googleapis.com/css2?family=League+Gothic&family=Open+Sans:wght@400;700&display=swap">
<style>
  :root{
    --teal:#3a8d8b;
    --teal-dark:#2c6f6d;
    --yellow:#e8e000;
    --orange:#f39020;
    --white:#ffffff;
    --paper:#ffffff;
  }
  *{box-sizing:border-box;margin:0;padding:0}
  html,body{width:1200px;height:487px;overflow:hidden;background:var(--paper)}
  .canvas{position:relative;width:1200px;height:487px;overflow:hidden;background:var(--paper)}

  /* Umschlag */
  .wrap{position:absolute;left:0;top:0;width:804px;height:487px;background:var(--teal)}
  .back{position:absolute;left:0;top:0;width:334px;height:487px}
  .back__title{position:absolute;left:57px;top:58px;font-family:"League Gothic",sans-serif;font-weight:400;font-size:25px;line-height:1;color:var(--white);white-space:nowrap;transform:scaleX(.8);transform-origin:0 0}
  .back__title .hl{color:var(--yellow)}
  .back__text{position:absolute;left:57px;top:100px;width:228px;font-family:"Open Sans",sans-serif;font-size:7.7px;line-height:9.7px;color:var(--white)}
  .back__text p{margin-bottom:9.7px}
  .back__text strong{font-weight:700}

  .brand{position:absolute;display:flex;align-items:center;justify-content:center;gap:5px;background:var(--orange);color:var(--white);font-family:"Open Sans",sans-serif;font-weight:400}
  .brand__dot{width:14px;height:14px;border-radius:50%;background:var(--white);flex:none}
  .brand--back{left:57px;top:418px;width:80px;height:33px;font-size:11px}

  .spine{position:absolute;left:334px;top:0;width:33px;height:487px;background:var(--yellow)}
  .spine__title{position:absolute;left:7px;top:38px;writing-mode:vertical-rl;font-family:"League Gothic",sans-serif;font-size:21px;line-height:1;color:var(--teal);letter-spacing:.3px;white-space:nowrap;transform:scaleY(.84);transform-origin:0 0}
  .spine__foot{position:absolute;left:0;top:368px;width:33px;height:119px;background:var(--orange)}
  .spine__brand{position:absolute;left:8px;top:28px;display:flex;flex-direction:column;align-items:center;gap:5px;color:var(--white);font-family:"Open Sans",sans-serif;font-size:11px}
  .spine__brand span{writing-mode:vertical-rl}
  .spine__brand .brand__dot{width:13px;height:13px}

  /* Vorderseite */
  .front{position:absolute;left:367px;top:0;width:437px;height:487px;background:var(--teal);overflow:hidden}
  .brand--front{left:257px;top:0;width:86px;height:33px;font-size:11px}
  .art{position:absolute;background:linear-gradient(160deg,#4f9e9b,var(--teal-dark));border-radius:6px;opacity:.9}
  .slashes{position:absolute;left:0;top:0;width:437px;height:487px}
  .front__title{position:absolute;left:38px;font-family:"League Gothic",sans-serif;font-weight:400;line-height:1;white-space:nowrap;transform-origin:0 0}
  .front__title--top{top:163px;font-size:96px;color:var(--white);transform:scaleX(.75)}
  .front__title--bottom{top:240px;font-size:80px;color:var(--yellow);transform:scaleX(.8)}
  .front__subtitle{position:absolute;left:0;width:437px;top:440px;text-align:center;font-family:"League Gothic",sans-serif;font-size:17px;letter-spacing:1px;color:var(--white);white-space:nowrap}

  /* Vorschau der Vorderseite */
  .preview{position:absolute;left:858px;top:100px;width:265px;height:295px;overflow:hidden}
  .preview .front{left:0;top:0;transform:scale(.606);transform-origin:0 0}
</style>
</head>
<body>
<div class="canvas">

  <section class="wrap">
    <div class="back">
      <h2 class="back__title">WERDEN SIE UNS <span class="hl">ALLES WEGNEHMEN?</span></h2>
      <div class="back__text">
        <p>Es ist jetzt Zeit zu Handel und sich mit dem Thema Finanzen auseinander zu setzen. Wir befinden uns in der größten Umverteilung von Geld in der gesamten Geschichte. Wer die finanzielle Eigenverantwortung nicht übernimmt, der wird definitiv als Verlierer Nachhause gehen. Und wir reden hier nicht nur von ein paar Euro, sondern möglicherweise von allem was man besitzt.</p>
        <p>Du findest in diesem Buch den geschichtlichen Hintergrund zum Geldsystem, erfährst alles über Inflation und die aktuelle Finanzpolitik. Wir geben konkrete Lösungen, aus unserer gelebten 25 jährigen Finanzerfahrung.</p>
        <p>Wir liefern Dir Fakten z.B. zum Thema Enteignung, welche vor Corona noch als wilde Versicherungstheorie gegolten hätte.</p>
        <p><strong>Du willst Dein Kapital sichern, willst das System verstehen, möchtest wissen welche Rolle Gold und Rohstoffe spielen und das Ganze kurz und verständlich?</strong></p>
        <p><strong>Dann ist das Dein Buch!</strong></p>
      </div>
      <div class="brand brand--back"><span class="brand__dot"></span>Aurelix</div>
    </div>

    <div class="spine">
      <div class="spine__title">WERDEN SIE UNS ALLES WEGNEHMEN</div>
      <div class="spine__foot">
        <div class="spine__brand"><span class="brand__dot"></span><span>Aurelix</span></div>
      </div>
    </div>

    <div class="front">
      <div class="brand brand--front"><span class="brand__dot"></span>Aurelix</div>
      <div class="art" style="left:45px;top:66px;width:82px;height:84px" role="img" aria-label="Illustration: Smartphone mit Bankkarte und Beleg"></div>
      <div class="art" style="left:155px;top:52px;width:82px;height:100px" role="img" aria-label="Illustration: Münzstapel und Kartenterminal"></div>
      <div class="art" style="left:270px;top:62px;width:96px;height:92px" role="img" aria-label="Illustration: Geldtransporter und Geldscheinbündel"></div>
      <div class="art" style="left:44px;top:335px;width:90px;height:88px" role="img" aria-label="Illustration: Bankgebäude"></div>
      <div class="art" style="left:155px;top:332px;width:92px;height:92px" role="img" aria-label="Illustration: Geldautomaten"></div>
      <div class="art" style="left:280px;top:318px;width:72px;height:106px" role="img" aria-label="Illustration: Münzen fallen in eine Spardose"></div>
      <svg class="slashes" viewBox="0 0 437 487" aria-hidden="true">
        <g stroke="var(--yellow)" stroke-width="9" stroke-linecap="round">
          <line x1="47" y1="144" x2="129" y2="69"/>
          <line x1="157" y1="144" x2="239" y2="69"/>
          <line x1="275" y1="144" x2="357" y2="69"/>
          <line x1="47" y1="414" x2="129" y2="338"/>
          <line x1="157" y1="414" x2="239" y2="338"/>
          <line x1="275" y1="414" x2="357" y2="338"/>
        </g>
      </svg>
      <h1 class="front__title front__title--top">WERDEN SIE UNS</h1>
      <div class="front__title front__title--bottom">ALLES WEGNEHMEN?</div>
      <p class="front__subtitle">Das Finanz-System verstehen und Ihr Kapital sichern!</p>
    </div>
  </section>

  <section class="preview" aria-label="Vorderseite">
    <div class="front">
      <div class="brand brand--front"><span class="brand__dot"></span>Aurelix</div>
      <div class="art" style="left:45px;top:66px;width:82px;height:84px" role="img" aria-label="Illustration: Smartphone mit Bankkarte und Beleg"></div>
      <div class="art" style="left:155px;top:52px;width:82px;height:100px" role="img" aria-label="Illustration: Münzstapel und Kartenterminal"></div>
      <div class="art" style="left:270px;top:62px;width:96px;height:92px" role="img" aria-label="Illustration: Geldtransporter und Geldscheinbündel"></div>
      <div class="art" style="left:44px;top:335px;width:90px;height:88px" role="img" aria-label="Illustration: Bankgebäude"></div>
      <div class="art" style="left:155px;top:332px;width:92px;height:92px" role="img" aria-label="Illustration: Geldautomaten"></div>
      <div class="art" style="left:280px;top:318px;width:72px;height:106px" role="img" aria-label="Illustration: Münzen fallen in eine Spardose"></div>
      <svg class="slashes" viewBox="0 0 437 487" aria-hidden="true">
        <g stroke="var(--yellow)" stroke-width="9" stroke-linecap="round">
          <line x1="47" y1="144" x2="129" y2="69"/>
          <line x1="157" y1="144" x2="239" y2="69"/>
          <line x1="275" y1="144" x2="357" y2="69"/>
          <line x1="47" y1="414" x2="129" y2="338"/>
          <line x1="157" y1="414" x2="239" y2="338"/>
          <line x1="275" y1="414" x2="357" y2="338"/>
        </g>
      </svg>
      <div class="front__title front__title--top">WERDEN SIE UNS</div>
      <div class="front__title front__title--bottom">ALLES WEGNEHMEN?</div>
      <p class="front__subtitle">Das Finanz-System verstehen und Ihr Kapital sichern!</p>
    </div>
  </section>

</div>
</body>
</html>
```